Elegant invitation for prestigious fund raising event

Background
The Lanterns of Grace is a very prestigious fund raising event. It is a sit down dinner, gala type evening with a presentation and auction.
There are three of these event being held at venues around western North Carolina. The areas where these are being held all have one thing in common, they are in the Appalachian Mountains and the craft of quilt making. As you will see from the Concept Boards attached why a mountain theme and quilt “design feel” is being used. One very important point - we don’t want this design to look like an actual quilt.

See the concept board on page 4, which we can’t use that is from another artist but is one good interpretation of the idea and one way to stylize the picture with a “quilt” interpretation and feel. We do not want a literal quilt representation but are looking for an artistic way on how best to interpret what the quilt represents - the feel of “stitching together” the different things across our region that make us all unique but yet bind us all as one.

The Brief:
We want to develop an elegant invitation for these events.
We have develop as save the date (attached) and all we want to use of this is the wording “Lanterns of Grace” we do not like the icon above it.
Also attached is the wording for the invitation, along with the new picture we want to use (taken from the inspiration boards)

Size, fold, color and paper:

Around 5x7 inches, but open to any dimension if you have an idea that will work in a totally different size. Ideally try and stick to something that will fit a standard envelope so that we don’t need to make a special envelope

Fold – up to you if it has a fold or not and which way it folds. Our thought is that it will need a fold to keep it up market but open to any suggestions.
We are happy to print this on a textured paper if you have suggestions. It will be professionally digital printed so the paper needs to be suitable for digital printing

Color. The inspiration boards show the color palette. We have started out in the save the dates with the navy with reversed out white but again totally up to you to use anything from that color palette.
Updates

Target Market(s)

Up market, around 50 - 65 years old, many are retired, very wealthy

Industry/Entity Type

Event

Requirements
Must have
• See brief attached
Nice to have
• See brief attached
Should not have
• See brief attached

```html
<!DOCTYPE html>
<html lang="en">
<head>
<meta charset="utf-8">
<title>Lanterns of Grace on the Plateau – Invitation</title>
<link href="https://fonts.googleapis.com/css2?family=Jost:wght@300;400;500&family=Cormorant+Garamond:wght@500&display=swap" rel="stylesheet">
<style>
  :root {
    --backdrop: #e4e4e4;
    --navy: #02497a;
    --paper: #ffffff;
    --ink: #3b4f8c;
    --ink-soft: #5a6aa0;
    --sky-top: #3f4f8a;
    --sky-glow: #d9a968;
    --ridge: #8a7bc0;
    --lake: #4b8fb5;
    --deep: #0f4a86;
    --white: #ffffff;
  }
  * { margin: 0; padding: 0; box-sizing: border-box; }
  html, body { width: 1200px; height: 1000px; overflow: hidden; }
  body {
    background: var(--backdrop);
    font-family: "Jost", sans-serif;
    position: relative;
  }
  .spread {
    position: absolute;
    left: 266px;
    width: 655px;
    height: 459px;
    display: flex;
    box-shadow: 0 2px 5px rgba(0,0,0,0.25);
  }
  .spread--outside { top: 35px; }
  .spread--inside { top: 503px; }
  .panel { position: relative; width: 327px; height: 100%; }
  .panel + .panel { width: 328px; border-left: 1px solid #c9c9c9; }

  .back-cover { background: var(--navy); }
  .back-cover__brand {
    position: absolute;
    top: 250px; left: 0; right: 0;
    display: flex; align-items: center; justify-content: center; gap: 7px;
    color: var(--white);
    font-weight: 400;
    font-size: 12px;
    letter-spacing: 0.06em;
    text-transform: uppercase;
  }
  .back-cover__brand::before {
    content: "";
    width: 9px; height: 9px;
    background: var(--white);
  }

  .front-cover { overflow: hidden; }
  .front-cover__art {
    position: absolute; inset: 0;
    background: linear-gradient(180deg,
      var(--sky-top) 0%,
      #7a6a9a 14%,
      var(--sky-glow) 34%,
      #a58fc8 48%,
      var(--ridge) 58%,
      var(--lake) 72%,
      #2f6aa6 84%,
      var(--deep) 100%);
  }
  .front-cover__title {
    position: absolute;
    top: 100px; left: 0; right: 0;
    text-align: center;
    color: var(--white);
  }
  .title__lead { font-weight: 300; font-size: 19px; letter-spacing: 0.03em; line-height: 1; }
  .title__main { font-weight: 400; font-size: 34px; letter-spacing: 0.02em; line-height: 1.05; }
  .title__place {
    display: flex; align-items: center; justify-content: center; gap: 6px;
    font-family: "Cormorant Garamond", serif;
    font-weight: 500; font-size: 13px; letter-spacing: 0.14em;
    margin-top: 4px;
  }
  .title__place::before, .title__place::after {
    content: ""; width: 46px; height: 1px; background: var(--white);
  }

  .inside-left { background: var(--paper); }
  .invitation {
    background: var(--paper);
    color: var(--ink);
    text-align: center;
    text-transform: uppercase;
  }
  .invitation__intro { position: absolute; top: 64px; left: 0; right: 0; font-size: 8px; letter-spacing: 0.14em; }
  .invitation__event { position: absolute; top: 91px; left: 0; right: 0; font-size: 11.5px; letter-spacing: 0.12em; line-height: 1.5; }
  .invitation__purpose { position: absolute; top: 140px; left: 0; right: 0; font-size: 8px; letter-spacing: 0.13em; line-height: 2.05; }
  .invitation__mark {
    position: absolute; top: 211px; left: 125px; width: 78px; height: 25px;
  }
  .invitation__details { position: absolute; top: 259px; left: 0; right: 0; font-size: 11px; font-weight: 500; letter-spacing: 0.1em; line-height: 1.72; }
  .invitation__notes {
    position: absolute; top: 354px; left: 0; right: 0;
    font-size: 8px; letter-spacing: 0.13em;
    display: flex; justify-content: center; align-items: center; gap: 10px;
  }
  .invitation__notes .dot { width: 4px; height: 4px; border-radius: 50%; background: var(--ink); }
  .invitation__beneficiary { position: absolute; top: 386px; left: 0; right: 0; font-size: 6px; letter-spacing: 0.14em; line-height: 2; color: var(--ink-soft); }
</style>
</head>
<body>
  <section class="spread spread--outside">
    <div class="panel back-cover">
      <p class="back-cover__brand">Ridgeview Valley Hospital</p>
    </div>
    <div class="panel front-cover">
      <div class="front-cover__art" role="img" aria-label="Quilt-inspired pixel pattern of layered mountain ridges under a sunset sky, in violet, gold, teal and navy"></div>
      <h1 class="front-cover__title">
        <span class="title__lead" style="display:block">LANTERNS OF</span>
        <span class="title__main" style="display:block">GRACE</span>
        <span class="title__place">PLATEAU</span>
      </h1>
    </div>
  </section>

  <section class="spread spread--inside">
    <div class="panel inside-left"></div>
    <div class="panel invitation">
      <p class="invitation__intro">You are invited to</p>
      <h2 class="invitation__event" style="font-weight:400">The second annual Lanterns of Grace<br>on the plateau.</h2>
      <p class="invitation__purpose">Please join us for an elegant<br>and entertaining affair benefiting<br>the healthcare in our region.</p>
      <svg class="invitation__mark" viewBox="0 0 78 25" role="img" aria-label="Small mountain peak emblem">
        <rect width="78" height="25" rx="3" fill="#3b4f8c" opacity="0.18"/>
      </svg>
      <p class="invitation__details">6th of June, 2016<br>The Farm at Laurel Creek Inn<br>Beginning at 5:30pm<br>Valet parking</p>
      <p class="invitation__notes"><span>Cocktail attire</span><span class="dot"></span><span>Valet parking</span></p>
      <p class="invitation__beneficiary">All proceeds from the night will go<br>to benefit Ridgeview Valley Hospital</p>
    </div>
  </section>
</body>
</html>
```